Concrete Grinding and Polishing company business card with logo, based in Australia.

We need a business card design along with logo for a new company based in Melbourne called BrightLap. We specialise in the grinding and polishing of concrete. Polished concrete is durable, easy to maintain, cost effective, dust proof, has increased light reflectivity, and is slip resistant, among other benefits. In short, polished concrete is a popular flooring solution because of its practical advantages, as well as it's decorative appeal.

Industry/Entity Type

Business

Requirements
Must have
• It must have the company name(BrightLap) as well as the slogan: A Cut Above The Rest.
Nice to have
• Something that symbolises polished concrete. Would also like it to have a silver background with black writing, if possible.

```html
<!DOCTYPE html>
<html lang="en">
<head>
<meta charset="utf-8">
<title>BrightLap – Business Card Concepts</title>
<link rel="stylesheet" href="https://fonts.googleapis.com/css2?family=Source+Sans+3:wght@400&display=swap">
<style>
  :root {
    --page: #ffffff;
    --steel-mid: #8b989d;
    --steel-dark: #4a555a;
    --steel-soft: #9ba7ab;
    --steel-deep: #56626a;
    --steel-shine: #f3f7f7;
    --steel-grey: #7f8c90;
    --steel-end: #b9c5c7;
    --ink-dark: #121416;
    --ink-steel: #2b3236;
  }
  html, body {
    margin: 0;
    padding: 0;
    overflow: hidden;
    background: var(--page);
  }
  .canvas {
    position: relative;
    width: 1200px;
    height: 800px;
    background: var(--page);
    overflow: hidden;
    font-family: "Source Sans 3", sans-serif;
  }
  .card {
    position: absolute;
    width: 607px;
    height: 316px;
    background: linear-gradient(to right,
      var(--steel-mid) 0%,
      var(--steel-dark) 20%,
      var(--steel-soft) 37%,
      var(--steel-deep) 52%,
      var(--steel-soft) 62%,
      var(--steel-shine) 72%,
      var(--steel-grey) 88%,
      var(--steel-end) 100%);
  }
  .card--first { left: 275px; top: 34px; }
  .card--second { left: 277px; top: 454px; }
  .card__name {
    position: absolute;
    left: 37px;
    top: 10px;
    margin: 0;
    font-size: 104px;
    font-weight: 400;
    line-height: 1;
    letter-spacing: 1px;
    white-space: nowrap;
  }
  .card__tagline {
    position: absolute;
    left: 0;
    right: 0;
    top: 228px;
    margin: 0;
    text-align: center;
    font-size: 40px;
    font-weight: 400;
    letter-spacing: 2px;
    line-height: 1;
  }
  .card--first .card__name,
  .card--first .card__tagline { color: var(--ink-steel); }
  .card--second .card__name,
  .card--second .card__tagline { color: var(--ink-dark); }
</style>
</head>
<body>
  <main class="canvas">
    <section class="card card--first">
      <h1 class="card__name">BrightLap</h1>
      <p class="card__tagline">A cut above the rest</p>
    </section>
    <section class="card card--second">
      <h2 class="card__name">BrightLap</h2>
      <p class="card__tagline">A cut above the rest</p>
    </section>
  </main>
</body>
</html>
```